New Corporate Email Signature with Custom GIF Tavik Electric LLC & Tavik Fire & Security

Project Overview
Tavik Electric LLC and Tavik Fire & Security are seeking a professional, polished, and technically robust corporate email signature design. The project has two integrated deliverables:
A custom animated GIF representing both sides of our business
A complete corporate email signature layout designed for real-world compatibility (Gmail, Outlook, iOS, Android)
Our brand aesthetic is corporate, conservative, and clean. We value clarity, trust, professionalism, and subtle creativity β€” nothing overly flashy or cartoonish.
This design will be used across the entire company and must be visually aligned with our brand while remaining technically dependable.

PART 1 β€” Animated GIF Requirements
The GIF will be the core visual anchor of the new signature.
It must be clean, smooth, subtle, and optimized for email use.
βš™ Technical Requirements
Max file size: 150–200 KB (smaller is better)
Dimensions: approx 300px width (flexible, but must look good small)
Looping: continuous loop
Style: professional, minimalistic transitions

No rapid flashing or harsh animations
Must export cleanly into a format email clients accept

🎞 GIF Animation Sequence
Phase 1 β€” Tavik Electric (TE)
Use the yellow β€œTE” avatar logo (provided).
Animation flow:
TE avatar appears
Full name β€œTavik Electric LLC” slides in, fades in, or otherwise appears smoothly
A scrolling or cycling list of service offerings displays:
EV Charging Stations
Generator & Transformers
Testing & Troubleshooting
LED Lighting Upgrades
After the list is shown, the entire TE segment fades out

Phase 2 β€” Tavik Fire & Security (TF)
Use the red β€œTF” avatar logo (provided).
Animation flow mirrors Phase 1:
TF avatar appears
Full name β€œTavik Fire & Security” slides/fades in
Scrolling or cycling list of services displays:
Fire Alarm Upgrades
BKDU 38 Test & Inspect
Security Surveillance Systems
Access Control Systems
Data & Fiber Optic Cabling
Fade out β†’ loop back to TE
Creative Direction

Designers are encouraged to use:
Clean transitions
Soft fades
Professional typography
Modern minimalism
Consistent brand colors
High clarity at small sizes

Avoid:
Busy motion
Hard flashes
Excessive text overlays
Overly long transitions

The goal: a smooth, corporate-grade rotation that fits seamlessly into an email signature.

PART 2 β€” Corporate Email Signature Design

The signature must be visually appealing, brand-aligned, and structurally bulletproof across all major email systems.
πŸ“ Required Elements
πŸ‘€ Left Side Content
Circular headshot (we will supply final photos)
Social media icons with embedded URLs:
Facebook
LinkedIn
Google Business Profile
Instagram

Icons should be clean, modern, and in alignment with brand colors
πŸ“„ Right Side Content
Name
Title
Tavik Electric LLC / Tavik Fire & Security (depending on user)
Phone number
Email address
License# 48263
Physical office address: 584 Marrowgate Rd, Kellmont PA 08391

Small CTA for newsletter signup (button or micro-banner)

🏒 Branding Assets Provided

You will receive:
TE avatar logo
TF avatar logo
Full-name TE logo
Full-name TF logo

These should be incorporated naturally and professionally.

Design Requirements

Conservative corporate styling

Clean typography

Balanced use of white space

Professional hierarchy

Light and dark mode compatibility preferred

Layout should not rely on one large image

All images should export cleanly for hosting on servers/CDN

Avoid overly tall signatures

The final signature must present as modern, trustworthy, and technically reliable across platforms.

πŸ§ͺ Compatibility Requirements

The signature must display correctly in:

Gmail (web and mobile)

Outlook (desktop & online)

Apple Mail

iPhone Mail

Android mail apps

Designers must avoid DIV-based layouts and instead propose a layout that can be implemented using table-based HTML, which is the industry standard for email compatibility.

You do not need to build the HTML β€” only supply the final layered design (PSD/AI/Figma) plus a clear structural layout that can be converted to HTML later.

πŸ“¦ Deliverables
1. Animated GIF

Final optimized GIF

Source file (After Effects, Photoshop, or equivalent)

Export guidelines so we can reproduce future versions

2. Email Signature Design

Full static design mockup

Modular layout for each employee

Icon set for social media

Newsletter CTA element

Clear spacing, alignment, and typography specifications

All source files (PSD, AI, Figma, etc.)

🧭 Creative Guidance Summary

We want:
βœ” Modern
βœ” Corporate
βœ” Minimalistic
βœ” Professional
βœ” Clean motion
βœ” Consistent branding
βœ” Email-safe elements

We do not want:
✘ Flashy marketing look
✘ Overly colorful or playful styles
✘ Hard-to-read fonts
✘ Heavy animation
✘ Oversized signatures

πŸ›  Tools & Format Flexibility

We allow full creative freedom regarding:

Animation style

Typography choices

Structuring of the two-column layout

How the service lists scroll or cycle

As long as the end result is clean, brand-aligned, professional, and email-compatible.

πŸ’¬ Final Note to Designers

We encourage creativity within the boundaries of corporate professionalism.
This signature will represent our company every time an email is sent β€” it must communicate trust, clarity, expertise, and brand strength.

```html
<!DOCTYPE html>
<html lang="en">
<head>
<meta charset="utf-8">
<title>Tavik Email Signatures – Part 2</title>
<link rel="stylesheet" href="https://fonts.googleapis.com/css2?family=Orbitron:wght@700;900&family=Montserrat:wght@500;600;700&display=swap">
<style>
  :root {
    --page-bg: #ffffff;
    --ink: #1a1e1f;
    --panel-dark: #1a1e1f;
    --band-gray: #4a5558;
    --white: #ffffff;
    --fire-red: #e0202e;
    --electric-yellow: #ecd213;
    --photo-warm: #c9a48c;
    --photo-deep: #4a3630;
  }
  * { box-sizing: border-box; margin: 0; padding: 0; }
  html, body { width: 1200px; height: 1200px; overflow: hidden; background: var(--page-bg); }
  body { position: relative; font-family: "Montserrat", Arial, sans-serif; }

  .sheet-title {
    position: absolute; top: 126px; left: 0; width: 1200px;
    text-align: center; font-family: "Orbitron", Arial, sans-serif;
    font-weight: 900; font-size: 62px; line-height: 72px; color: var(--ink); letter-spacing: 2px;
  }

  .signature {
    position: absolute; left: 195px; width: 817px; height: 272px;
    background: var(--panel-dark);
    box-shadow: 6px 7px 9px rgba(0,0,0,0.45);
    overflow: hidden;
  }
  .signature--fire { top: 297px; --accent: var(--fire-red); --on-accent: var(--white); }
  .signature--electric { top: 679px; --accent: var(--electric-yellow); --on-accent: var(--ink); }

  .brand-mark {
    position: absolute; left: 12px; top: 10px; width: 46px; height: 24px;
    font-family: "Orbitron", Arial, sans-serif; font-weight: 900; font-size: 20px;
    color: var(--white); line-height: 24px; text-align: center;
  }
  .company-name {
    position: absolute; left: 83px; top: 10px;
    font-family: "Orbitron", Arial, sans-serif; font-weight: 900; font-size: 19px;
    color: var(--white); letter-spacing: 0.5px; line-height: 24px; text-transform: uppercase;
    white-space: nowrap;
  }
  .person-name {
    position: absolute; right: 31px; top: 10px;
    font-family: "Orbitron", Arial, sans-serif; font-weight: 900; font-size: 21px;
    color: var(--accent); letter-spacing: 1px; line-height: 24px; text-transform: uppercase;
    white-space: nowrap;
  }

  .social-rail {
    position: absolute; left: 0; top: 42px; width: 68px; height: 230px;
    background: var(--accent);
  }
  .social-rail__label {
    position: absolute; top: 5px; left: 0; width: 68px; text-align: center;
    font-family: "Orbitron", Arial, sans-serif; font-weight: 900; font-size: 11px;
    line-height: 14px; color: var(--on-accent); text-transform: uppercase;
  }
  .social-rail__link {
    position: absolute; left: 14px; width: 41px; height: 41px; border-radius: 50%;
    background: var(--on-accent); display: block;
  }

  .headshot-area {
    position: absolute; left: 68px; top: 42px; width: 302px; height: 230px;
    background: var(--white);
  }
  .headshot {
    position: absolute; left: 45px; top: 12px; width: 206px; height: 206px;
    border-radius: 50%; border: 12px solid var(--panel-dark);
    background: radial-gradient(circle at 50% 45%, var(--photo-warm) 0%, #8a6a5c 45%, var(--photo-deep) 80%);
  }

  .rule {
    position: absolute; left: 370px; top: 42px; width: 416px; height: 2px; background: var(--accent);
  }
  .job-title {
    position: absolute; right: 31px; top: 54px;
    font-size: 14px; font-weight: 500; color: var(--white); letter-spacing: 0.5px;
  }
  .contact-pill {
    position: absolute; left: 384px; top: 58px; width: 42px; height: 150px;
    border-radius: 21px; background: var(--accent); color: var(--on-accent);
  }
  .contact-pill svg { position: absolute; left: 11px; width: 20px; height: 20px; }
  .contact-line {
    position: absolute; left: 448px; font-size: 14px; font-weight: 500;
    color: var(--white); line-height: 18px; white-space: nowrap;
  }

  .newsletter-cta {
    position: absolute; left: 370px; top: 222px; width: 447px; height: 39px;
    background: var(--band-gray); color: var(--white);
    font-weight: 700; font-size: 22px; line-height: 39px; text-align: center;
    padding-left: 30px; letter-spacing: 0.3px; white-space: nowrap;
  }
</style>
</head>
<body>
  <h1 class="sheet-title">PART 2</h1>

  <!-- Fire & Security signature -->
  <section class="signature signature--fire">
    <div class="brand-mark">TF</div>
    <div class="company-name">Tavik Fire &amp; Security</div>
    <div class="person-name">Name Surname</div>

    <nav class="social-rail" aria-label="Social profiles">
      <div class="social-rail__label">Click<br>Below</div>
      <a class="social-rail__link" style="top:35px" aria-label="Business profile"></a>
      <a class="social-rail__link" style="top:83px" aria-label="Social profile"></a>
      <a class="social-rail__link" style="top:130px" aria-label="Professional network"></a>
      <a class="social-rail__link" style="top:178px" aria-label="Photo profile"></a>
    </nav>

    <div class="headshot-area">
      <div class="headshot" role="img" aria-label="Circular headshot of the team member"></div>
    </div>

    <div class="rule"></div>
    <div class="job-title">GENERAL MANAGER</div>

    <div class="contact-pill">
      <svg viewBox="0 0 20 20" style="top:16px" fill="currentColor"><path d="M5 2h3l1.5 4-2 1.3a10 10 0 0 0 5.2 5.2L14 10.5l4 1.5v3a2 2 0 0 1-2 2A14 14 0 0 1 3 4a2 2 0 0 1 2-2z"/></svg>
      <svg viewBox="0 0 20 20" style="top:45px" fill="none" stroke="currentColor" stroke-width="1.6"><rect x="2" y="4" width="16" height="12"/><polyline points="2,4 10,11 18,4"/><polyline points="2,16 8,9.5"/><polyline points="18,16 12,9.5"/></svg>
      <svg viewBox="0 0 20 20" style="top:79px" fill="currentColor"><circle cx="10" cy="6" r="4"/><path d="M2 19c0-5 3.5-7 8-7s8 2 8 7z"/></svg>
      <svg viewBox="0 0 20 20" style="top:113px" fill="currentColor"><path d="M10 1a6 6 0 0 0-6 6c0 4.5 6 12 6 12s6-7.5 6-12a6 6 0 0 0-6-6zm0 8.5a2.5 2.5 0 1 1 0-5 2.5 2.5 0 0 1 0 5z"/></svg>
    </div>
    <div class="contact-line" style="top:75px">+1 1234 123456</div>
    <div class="contact-line" style="top:104px">support@tavikelectricllc.com</div>
    <div class="contact-line" style="top:138px">License #48263</div>
    <div class="contact-line" style="top:172px">584 Marrowgate Rd, Kellmont PA 08391</div>

    <div class="newsletter-cta">JOIN OUR NEWSLETTER!!</div>
  </section>

  <!-- Electric signature -->
  <section class="signature signature--electric">
    <div class="brand-mark">TE</div>
    <div class="company-name">Tavik Electric LLC</div>
    <div class="person-name">Name Surname</div>

    <nav class="social-rail" aria-label="Social profiles">
      <div class="social-rail__label">Click<br>Below</div>
      <a class="social-rail__link" style="top:35px" aria-label="Business profile"></a>
      <a class="social-rail__link" style="top:83px" aria-label="Social profile"></a>
      <a class="social-rail__link" style="top:130px" aria-label="Professional network"></a>
      <a class="social-rail__link" style="top:178px" aria-label="Photo profile"></a>
    </nav>

    <div class="headshot-area">
      <div class="headshot" role="img" aria-label="Circular headshot of the team member"></div>
    </div>

    <div class="rule"></div>
    <div class="job-title">GENERAL MANAGER</div>

    <div class="contact-pill">
      <svg viewBox="0 0 20 20" style="top:16px" fill="currentColor"><path d="M5 2h3l1.5 4-2 1.3a10 10 0 0 0 5.2 5.2L14 10.5l4 1.5v3a2 2 0 0 1-2 2A14 14 0 0 1 3 4a2 2 0 0 1 2-2z"/></svg>
      <svg viewBox="0 0 20 20" style="top:45px" fill="none" stroke="currentColor" stroke-width="1.6"><rect x="2" y="4" width="16" height="12"/><polyline points="2,4 10,11 18,4"/><polyline points="2,16 8,9.5"/><polyline points="18,16 12,9.5"/></svg>
      <svg viewBox="0 0 20 20" style="top:79px" fill="currentColor"><circle cx="10" cy="6" r="4"/><path d="M2 19c0-5 3.5-7 8-7s8 2 8 7z"/></svg>
      <svg viewBox="0 0 20 20" style="top:113px" fill="currentColor"><path d="M10 1a6 6 0 0 0-6 6c0 4.5 6 12 6 12s6-7.5 6-12a6 6 0 0 0-6-6zm0 8.5a2.5 2.5 0 1 1 0-5 2.5 2.5 0 0 1 0 5z"/></svg>
    </div>
    <div class="contact-line" style="top:75px">+1 1234 123456</div>
    <div class="contact-line" style="top:104px">support@tavikelectricllc.com</div>
    <div class="contact-line" style="top:138px">License #48263</div>
    <div class="contact-line" style="top:172px">584 Marrowgate Rd, Kellmont PA 08391</div>

    <div class="newsletter-cta">JOIN OUR NEWSLETTER!!</div>
  </section>
</body>
</html>
```